Natural Immune System Booster

We need a pharmaceutical type box and label design for a vitamin supplement product. Pravolex is in process of being trademarked and should therefore carry the TM symbol. It is comprised of a special blend of over 20 vitamins, herbs and minerals with a High strength vitamin C booster. The tag line should read. The No.1 Natural Support For Your Immune System. Each tube contains 10 tablets. A bar code will be placed on the box carton. We prefer bright and vivid colours, preferably a mix of electric purple, yellow and orange mix. We have three flavours, summer berry (strawberry), tropical fruit and juicy orange - the box and label should indicate the flavours in a creative design element. Effervescent tabelts should be clearly marked on the box and label. The ingredients and instructions should be present on the box outer carton and also the label. We require an eye catching yet simple and bright design that pops off the shelf.
Updates

Target Market(s)

Target customers are male and female 20 - 60+ that live in Western countries that handle household budgets.

Industry/Entity Type

Pharmaceutical

Requirements
Must have
• Please see current box design, all necessary elements and specifications are included here. We require same to be placed on new design.

I have attached a txt file of the supplement facts and other details that are required for both the label and the box

```html
<!DOCTYPE html>
<html lang="en">
<head>
<meta charset="utf-8">
<title>Pravolex Vitamin Supplement – Summer Berry Label</title>
<link rel="stylesheet" href="https://fonts.googleapis.com/css2?family=Raleway:wght@200;300;400;700;800&family=Kalam:wght@700&display=swap">
<style>
  :root {
    --purple-deep: #5b2483;
    --purple-mid: #7a3598;
    --purple-light: #9a55b5;
    --purple-text: #7b2f92;
    --ink: #151515;
    --paper: #ffffff;
    --paper-shade: #dcdcdc;
    --orange: #f7a52f;
    --lavender: #e6d3f0;
  }
  * { margin: 0; padding: 0; box-sizing: border-box; }
  html, body { width: 1200px; height: 438px; overflow: hidden; background: var(--paper); }
  .label {
    position: relative;
    width: 1200px;
    height: 438px;
    overflow: hidden;
    font-family: "Raleway", sans-serif;
    background: linear-gradient(100deg, var(--purple-mid) 0%, var(--purple-deep) 100%);
  }
  .label__panel {
    position: absolute;
    inset: 0;
    width: 100%;
    height: 100%;
  }
  .label__art {
    position: absolute;
    left: 660px;
    top: 0;
    width: 400px;
    height: 438px;
    background: radial-gradient(ellipse 55% 60% at 45% 45%, rgba(230,211,240,0.75) 0%, rgba(180,130,205,0.45) 45%, rgba(122,53,152,0) 100%);
  }
  .brand {
    position: absolute;
    left: 26px;
    top: 52px;
    width: 604px;
    display: flex;
    align-items: center;
    gap: 14px;
  }
  .brand__name {
    font-weight: 300;
    font-size: 118px;
    line-height: 1;
    letter-spacing: 2px;
    color: var(--ink);
  }
  .brand__dot {
    width: 22px;
    height: 22px;
    border-radius: 50%;
    background: var(--purple-text);
    flex: none;
  }
  .product-type {
    position: absolute;
    left: 28px;
    top: 152px;
    font-weight: 300;
    font-size: 62px;
    line-height: 1;
    letter-spacing: 0.5px;
    color: var(--ink);
  }
  .tagline {
    position: absolute;
    left: 30px;
    top: 246px;
    width: 600px;
    text-align: center;
    color: var(--ink);
  }
  .tagline__rank {
    font-weight: 200;
    font-size: 68px;
    line-height: 1;
  }
  .tagline__rank strong { font-weight: 800; color: var(--purple-text); }
  .tagline__line {
    margin-top: 10px;
    font-weight: 400;
    font-size: 31px;
    line-height: 1.1;
  }
  .tagline__focus {
    font-weight: 700;
    font-size: 34px;
    line-height: 1.15;
    color: var(--purple-text);
  }
  .format-note {
    position: absolute;
    right: 18px;
    top: 14px;
    font-family: "Kalam", cursive;
    font-weight: 700;
    font-size: 22px;
    line-height: 1.05;
    text-align: center;
    color: var(--orange);
  }
  .flavour {
    position: absolute;
    right: 12px;
    top: 272px;
    text-align: right;
    color: var(--paper);
    line-height: 1;
  }
  .flavour__first { display: block; font-weight: 300; font-size: 38px; }
  .flavour__second { display: block; font-weight: 400; font-size: 52px; margin-top: 2px; }
  .count {
    position: absolute;
    right: 12px;
    top: 392px;
    width: 158px;
    height: 38px;
    border-radius: 19px;
    background: var(--paper);
    color: var(--purple-text);
    font-weight: 400;
    font-size: 26px;
    line-height: 38px;
    text-align: center;
  }
  .count strong { font-weight: 700; }
</style>
</head>
<body>
  <div class="label">
    <svg class="label__panel" viewBox="0 0 1200 438" aria-hidden="true">
      <defs>
        <linearGradient id="paperFill" x1="0" y1="0" x2="1" y2="0">
          <stop offset="0" stop-color="#ffffff"/>
          <stop offset="0.65" stop-color="#f6f6f6"/>
          <stop offset="1" stop-color="#d6d6d6"/>
        </linearGradient>
      </defs>
      <path d="M0 0 H585 Q665 220 598 438 H0 Z" fill="#b98fcf" opacity="0.6"/>
      <path d="M0 0 H572 Q650 220 588 438 H0 Z" fill="url(#paperFill)"/>
    </svg>

    <div class="label__art" role="img" aria-label="Effervescent tablets fizzing with rising bubbles and soft lilac flowers"></div>

    <div class="brand">
      <span class="brand__name">PRAVOLEX</span>
      <span class="brand__dot"></span>
    </div>
    <p class="product-type">VITAMIN SUPPLEMENT</p>

    <div class="tagline">
      <p class="tagline__rank">The <strong>No.1</strong></p>
      <p class="tagline__line">Natural Support For Your</p>
      <p class="tagline__focus">Immune System</p>
    </div>

    <p class="format-note">Effervescent<br>tablets</p>

    <p class="flavour">
      <span class="flavour__first">SUMMER</span>
      <span class="flavour__second">BERRY</span>
    </p>

    <p class="count"><strong>10</strong> tablets</p>
  </div>
</body>
</html>
```